3 in 1 website - Property Lens Studio + Keepsake Vault LLC + Marla's Field Shots

Help me simplify and organize my business life. I am a sports photographer (action, individual and teams), real estate photographer (stills and drones) and I transfer videos and photos to jump drives, along with photo restoration, etc. Currently, I have a functioning website for the transfer/restoration business at KeepsakeVaultLLC.example which was recently created and I like it. I have received several really good ideas for the Real Estate Photography portion! I don't have anything started for the Sports Pics. My vision possibly includes a main/home page giving people the option to choose real estate, sports or transfer/restoration. I just want them combined into one site....somehow to better organize my businesses and give me ONE place to keep to updated and check for communication. I just updated the brief again and added logo files for my "parent" company called "Keepsake Vault". I prefer this logo at the top of the main/home page, please. I previously uploaded the logo for Property Lens Studio which would be used with the real estate portion of my business. At this point, I don't have a logo for the sports photography portion.

Target Market(s)

Real Estate Agents and Brokers; Sports team, parents and boosters; Community members typically 40+ years old

Industry/Entity Type

Real Estate Photography; Local sports teams; Community members 40+ years old

Coding

Coded - Design and coding required

Number of Pages Required

3 page

Requirements
Must have
• At least one page for each area: real estate, sports, digital transfers. The real estate will need to connect to an account I have with QPN for checkout options. The sports page(s) will need to connect to a 3rd party service, also. The digital transfers, photo restorations, etc. would just need a way for them to request service.
Nice to have
• I currently have a website at KeepsakeVaultLLC.example for the digital transfer/photo restoration part of my business. I like this website but want it integrated with one main site for all 3 businesses.

```html
<!DOCTYPE html>
<html lang="en">
<head>
<meta charset="utf-8">
<title>Keepsake Vault — Property Lens Studio</title>
<link href="https://fonts.googleapis.com/css2?family=Poppins:wght@400;500;600;700&display=swap" rel="stylesheet">
<style>
:root{
  --red:#e3202a;
  --teal:#16a596;
  --ink:#1d1d1d;
  --text:#333;
  --muted:#555;
  --grey-bar:#dcdcdc;
  --grey-bg:#ececec;
  --card-head:#6d6d6d;
  --white:#fff;
  --line:#cfcfcf;
  --blue:#1a6fc4;
}
*{box-sizing:border-box;margin:0;padding:0}
html,body{width:1200px;height:4234px;overflow:hidden}
body{font-family:'Poppins',sans-serif;color:var(--text);background:var(--white);position:relative}
.abs{position:absolute}
.btn{position:absolute;display:flex;align-items:center;justify-content:center;font-size:11px;font-weight:600;text-transform:uppercase;letter-spacing:.2px;border-radius:3px;height:27px;white-space:nowrap}
.btn-red{background:var(--red);color:var(--white)}
.btn-outline{background:var(--white);color:var(--ink);border:1.5px solid var(--red)}
.btn-ghost{border:1.5px solid var(--white);color:var(--white)}
.section-title{position:absolute;left:0;width:1200px;text-align:center;font-size:33px;font-weight:600;color:var(--ink);line-height:1.2}

/* utility bar with business switcher */
.topbar{top:0;left:0;width:1200px;height:25px;background:var(--grey-bar);font-size:10px;color:var(--ink)}
.topbar .util{position:absolute;top:6px;display:flex;align-items:center;gap:6px;line-height:1}
.hub{position:absolute;left:112px;top:6px;display:flex;align-items:center;gap:10px;line-height:1;font-size:10px}
.hub-parent{font-weight:600;letter-spacing:.4px}
.hub-link{color:var(--muted)}
.hub-link.current{color:var(--red);font-weight:600}
.hub-sep{color:#999}

.nav{top:25px;left:0;width:1200px;height:61px;background:var(--white)}
.brand{position:absolute;left:112px;top:14px;display:flex;align-items:center;gap:7px}
.brand-mark{width:14px;height:14px;background:var(--red);border-radius:50%}
.brand-name{font-size:12px;font-weight:600;color:var(--red);line-height:1.15}
.brand-name small{display:block;font-size:8px;font-weight:600}
.menu{position:absolute;top:24px;left:466px;display:flex;gap:20px;font-size:10.5px;font-weight:500;color:var(--ink)}
.menu .active{color:var(--red)}
.nav-cta{left:928px;top:17px;background:var(--teal);color:var(--white);width:155px}

/* hero */
.hero{top:86px;left:0;width:1200px;height:544px;background:linear-gradient(180deg,#6b7a86 0%,#8c969c 45%,#4a5350 100%)}
.hero h1{position:absolute;top:228px;width:1200px;text-align:center;color:var(--white);font-size:48px;font-weight:700;line-height:1.2}
.hero p{position:absolute;top:303px;width:1200px;text-align:center;color:var(--white);font-size:19px;font-weight:600}

/* steps */
.steps{top:745px;left:130px;width:940px;display:flex;justify-content:space-between}
.step{width:205px;text-align:center;font-size:11px;line-height:1.65;color:var(--text)}
.step svg{display:block;margin:0 auto 20px;height:86px}
.step b{font-weight:600;color:var(--ink)}

/* packages */
.packages{top:990px;left:0;width:1200px;height:736px;background:var(--grey-bg)}
.card{position:absolute;top:1085px;width:219px;height:526px;background:var(--white);box-shadow:0 2px 6px rgba(0,0,0,.12)}
.card-head{height:160px;background:var(--card-head);color:var(--white);text-align:center}
.card-head svg{display:block;margin:0 auto;padding-top:26px;height:100px}
.card-head h3{font-size:15px;font-weight:500;margin-top:16px}
.price{display:flex;justify-content:space-between;padding:20px 14px 14px;font-size:15px;font-weight:500;color:var(--ink)}
.card ul{list-style:none;padding:0 14px 0 32px;font-size:9.6px;line-height:1.2;color:var(--text)}
.card li{position:relative;margin-bottom:8px}
.card li::before{content:"";position:absolute;left:-10px;top:3px;width:6px;height:6px;border-radius:50%;background:var(--ink)}

/* headshots */
.photo{position:absolute}
.headshots h2{position:absolute;left:610px;top:1800px;font-size:36px;font-weight:600;color:var(--ink);line-height:1.2}
.headshots .lead{position:absolute;left:614px;top:1860px;width:400px;font-size:15px;font-weight:500;color:var(--ink);line-height:1.3}
.headshots .inc{position:absolute;left:614px;top:1910px;font-size:13.5px;text-decoration:underline;color:var(--ink)}
.headshots ul{position:absolute;left:645px;top:1945px;font-size:10.5px;line-height:19px;color:var(--text);list-style:none}
.headshots li::before{content:"●";margin-right:4px;font-size:8px;margin-left:-12px}

/* why */
.why{top:2286px;left:124px;width:952px;display:flex;justify-content:space-between}
.why-item{width:222px;text-align:center}
.why-item svg{display:block;margin:0 auto;height:84px}
.why-item h4{margin-top:22px;font-size:14.5px;font-weight:500;color:var(--ink)}
.why-item p{margin-top:8px;font-size:10.8px;line-height:1.3;color:var(--muted);padding:0 12px}
.divider{top:2548px;left:122px;width:956px;height:1px;background:var(--line)}

/* clients */
.clients .label{position:absolute;left:126px;top:2590px;font-size:13px;font-weight:500;color:var(--muted)}
.clients h2{position:absolute;left:124px;top:2614px;font-size:35px;font-weight:700;line-height:1.05;color:var(--ink)}
.clients blockquote{position:absolute;left:126px;top:2704px;width:340px;font-size:16px;line-height:1.6;color:var(--text)}
.play{position:absolute;left:810px;top:2698px;width:66px;height:66px;border-radius:50%;border:3px solid var(--red)}
.play::after{content:"";position:absolute;left:25px;top:17px;border-left:20px solid var(--red);border-top:13px solid transparent;border-bottom:13px solid transparent}

/* testimonial band */
.band{top:2923px;left:0;width:1200px;height:368px;background:linear-gradient(180deg,#3e3c39 0%,#5c544c 55%,#2c2a28 100%)}
.avatar{position:absolute;left:556px;top:2975px;width:88px;height:88px;border-radius:50%;background:#9a8876;border:3px solid var(--white)}
.band-name{position:absolute;top:3076px;width:1200px;text-align:center;color:var(--white);font-size:18px}
.band-name b{font-weight:500}
.band-quote{position:absolute;left:390px;top:3108px;width:420px;text-align:center;color:var(--white);font-size:12px;line-height:1.55}
.arrow{position:absolute;top:3100px;width:14px;height:14px;border-left:3px solid var(--white);border-bottom:3px solid var(--white)}
.dots{position:absolute;top:3221px;left:572px;display:flex;gap:10px}
.dots i{width:11px;height:11px;border-radius:50%;border:1.5px solid var(--white)}
.dots i.on{background:var(--red);border-color:var(--red)}

/* partners */
.partners{top:3345px;left:120px;width:960px;display:flex;justify-content:space-between;align-items:center}
.partner{width:130px;height:96px;background:#d7dde3;border-radius:6px}

/* closing call to action */
.cta-dark{top:3497px;left:607px;width:593px;height:452px;background:linear-gradient(180deg,#4b4743 0%,#39352f 100%)}
.cta-title{position:absolute;left:673px;top:3636px;color:var(--white);font-size:36px;font-weight:600;line-height:1.25}

/* footer */
.footer-brand{top:3990px}
.footer-about{position:absolute;left:112px;top:4040px;width:270px;font-size:11px;line-height:1.7;color:var(--text)}
.fhead{position:absolute;top:3982px;font-size:14.5px;font-weight:600;color:var(--ink)}
.fhead u{text-decoration:none;border-bottom:2px solid var(--red)}
.quick{position:absolute;left:427px;top:4020px;list-style:none;font-size:10.5px;font-weight:500;line-height:28.7px;color:var(--ink)}
.contact{position:absolute;left:588px;top:4022px;font-size:11px;color:var(--ink);line-height:1}
.contact div{display:flex;align-items:center;gap:10px;margin-bottom:22px}
.news-input{position:absolute;left:844px;top:4017px;width:158px;height:30px;background:#eee;border:1px solid #ddd;font-size:11px;color:#999;padding:8px 8px}
.news-btn{left:1007px;top:4017px;width:81px;height:30px}
.news-sub{position:absolute;left:844px;top:4064px;font-size:14px;font-weight:600;color:var(--ink)}
.foot-line{top:4192px;left:48px;width:1102px;height:1px;background:var(--line)}
.copy{position:absolute;left:112px;top:4206px;font-size:10.5px;font-weight:500;color:var(--ink)}
.social{position:absolute;left:964px;top:4204px;display:flex;gap:10px}
.social i{width:18px;height:18px;border-radius:50%;border:1.5px solid var(--ink)}
</style>
</head>
<body>

<!-- utility bar: parent company and business switcher -->
<div class="abs topbar">
  <nav class="hub" aria-label="Keepsake Vault businesses">
    <span class="hub-parent">KEEPSAKE VAULT</span>
    <span class="hub-sep">|</span>
    <span class="hub-link current">Property Lens Studio</span>
    <span class="hub-sep">|</span>
    <span class="hub-link">Marla's Field Shots</span>
    <span class="hub-sep">|</span>
    <span class="hub-link">Transfers &amp; Restoration</span>
  </nav>
  <span class="util" style="left:690px"><svg width="10" height="10" viewBox="0 0 10 10"><circle cx="5" cy="3" r="2.5" fill="#555"/><path d="M0 10a5 4 0 0 1 10 0z" fill="#555"/></svg>LOG IN/REGISTER</span>
  <span class="util" style="left:842px"><svg width="12" height="10" viewBox="0 0 12 10"><path d="M6 0l6 5h-2v5H2V5H0z" fill="#555"/></svg>CLIENT PORTAL</span>
  <span class="util" style="left:980px"><svg width="10" height="10" viewBox="0 0 10 10"><path d="M2 0l2 2-1 2 3 3 2-1 2 2-2 2C4 10 0 6 0 2z" fill="#555"/></svg>555-014-2207</span>
</div>

<!-- navigation -->
<header class="abs nav">
  <div class="brand"><span class="brand-mark"></span><span class="brand-name">DANA WHITFIELD<small>Real Estate Photographer</small></span></div>
  <nav class="menu">
    <span class="active">HOME</span><span>SERVICES ▾</span><span>PROPERTY TYPE ▾</span><span>GALLERY ▾</span><span>PRICING ▾</span><span>LEARN</span>
  </nav>
  <span class="btn nav-cta">Schedule Your Shot</span>
</header>

<!-- hero -->
<section class="abs hero" role="img" aria-label="Modern multi-storey glass house at dusk with trees behind">
  <h1>Real Estate Photographer</h1>
  <p>Helping you connect home sellers with home buyers.</p>
</section>
<span class="btn btn-red" style="left:522px;top:441px;width:155px">Schedule Your Shot</span>

<!-- how we work -->
<h2 class="section-title" style="top:652px">How We Works</h2>
<div class="abs steps">
  <div class="step">
    <svg viewBox="0 0 90 86"><rect x="4" y="20" width="82" height="50" rx="3" fill="#1d1d1d"/><rect x="10" y="26" width="70" height="36" fill="#fff"/><rect x="14" y="30" width="34" height="6" fill="#1d1d1d"/><rect x="14" y="40" width="24" height="4" fill="#1d1d1d"/><rect x="14" y="48" width="24" height="4" fill="#1d1d1d"/><rect x="38" y="70" width="14" height="8" fill="#1d1d1d"/><rect x="28" y="78" width="34" height="4" fill="#1d1d1d"/><circle cx="66" cy="20" r="14" fill="#fff" stroke="#e3202a" stroke-width="4"/><path d="M60 22l5 5 8-10" stroke="#e3202a" stroke-width="4" fill="none"/></svg>
    First, <b>create an account</b> right here, on our website.
  </div>
  <div class="step">
    <svg viewBox="0 0 90 86"><rect x="6" y="10" width="70" height="62" rx="4" fill="#1d1d1d"/><rect x="12" y="24" width="58" height="42" fill="#fff"/><g fill="#1d1d1d"><rect x="16" y="28" width="9" height="7"/><rect x="29" y="28" width="9" height="7"/><rect x="42" y="28" width="9" height="7"/><rect x="55" y="28" width="9" height="7"/><rect x="16" y="40" width="9" height="7"/><rect x="29" y="40" width="9" height="7"/><rect x="16" y="52" width="9" height="7"/><rect x="29" y="52" width="9" height="7"/></g><circle cx="68" cy="64" r="17" fill="#e3202a"/><path d="M68 54v11h8" stroke="#fff" stroke-width="3" fill="none"/></svg>
    <b>Schedule your appointment</b> online in a few easy clicks.
  </div>
  <div class="step">
    <svg viewBox="0 0 90 86"><rect x="24" y="18" width="36" height="24" rx="3" fill="#1d1d1d"/><circle cx="34" cy="10" r="8" fill="none" stroke="#e3202a" stroke-width="4"/><circle cx="52" cy="10" r="8" fill="none" stroke="#e3202a" stroke-width="4"/><path d="M60 24l12-6v22l-12-6z" fill="#1d1d1d"/><path d="M42 42v40M42 46L26 82M42 46l16 36" stroke="#1d1d1d" stroke-width="4"/></svg>
    <b>We shoot your photos and video</b> and then have them edited and touched up in no time.
  </div>
  <div class="step">
    <svg viewBox="0 0 90 86"><rect x="4" y="8" width="82" height="54" rx="3" fill="#1d1d1d"/><rect x="10" y="14" width="70" height="40" fill="#fff"/><rect x="38" y="62" width="14" height="10" fill="#1d1d1d"/><rect x="28" y="72" width="34" height="5" fill="#1d1d1d"/><rect x="30" y="22" width="36" height="24" fill="#e3202a"/><path d="M30 22l18 13 18-13" stroke="#fff" stroke-width="3" fill="none"/></svg>
    <b>Receive your content</b> by 6:00pm the next business day (2-3 business days for video).
  </div>
</div>
<span class="btn btn-red" style="left:539px;top:921px;width:121px">Get Started</span>

<!-- packages -->
<section class="abs packages"></section>
<h2 class="section-title" style="top:1014px">Packages</h2>

<div class="card" style="left:130px">
  <div class="card-head">
    <svg viewBox="0 0 60 70"><rect x="18" y="8" width="24" height="24" rx="4" fill="#fff"/><rect x="20" y="34" width="20" height="30" fill="#fff"/><rect x="6" y="14" width="8" height="3" fill="#16a596"/><rect x="46" y="14" width="8" height="3" fill="#16a596"/></svg>
    <h3>The Ultimate Package</h3>
  </div>
  <div class="price"><span>Price</span><span>$150</span></div>
  <ul>
    <li>Up to 25 ClearView+ Still Images</li><li>Branded &amp; Non-Branded Property Website Links</li><li>Company Branding</li><li>Agent photo &amp; contact information</li><li>Link to agent Property Website gallery</li><li>Property description &amp; details</li><li>Weekly Seller's report</li><li>Posting to MLS</li><li>High resolution printable still photos</li><li>Unlimited text updates</li><li>Music enabled</li>
  </ul>
</div>

<div class="card" style="left:370px">
  <div class="card-head">
    <svg viewBox="0 0 70 70"><path d="M22 10l13 10 13-10" stroke="#16a596" stroke-width="4" fill="none"/><circle cx="35" cy="30" r="8" fill="#fff"/><circle cx="18" cy="36" r="7" fill="#fff"/><circle cx="52" cy="36" r="7" fill="#fff"/><path d="M22 64a13 14 0 0 1 26 0z M4 64a14 14 0 0 1 22-10v10z M66 64a14 14 0 0 0-22-10v10z" fill="#fff"/></svg>
    <h3>The VIP Package</h3>
  </div>
  <div class="price"><span>Price</span><span>$200</span></div>
  <ul>
    <li>Up to 50 ClearView+ Still Images</li><li>Branded &amp; Non-Branded Property Website Links</li><li>Company Branding</li><li>Agent photo &amp; contact information</li><li>Link to agent Property Website gallery</li><li>Property description &amp; details</li><li>Weekly Seller's report</li><li>Posting to MLS</li><li>High resolution printable still photos</li><li>Unlimited text updates</li><li>Music enabled</li>
  </ul>
</div>

<div class="card" style="left:610px">
  <div class="card-head">
    <svg viewBox="0 0 70 70"><g fill="none" stroke="#fff" stroke-width="3"><circle cx="14" cy="16" r="9"/><circle cx="56" cy="16" r="9"/><circle cx="14" cy="54" r="9"/><circle cx="56" cy="54" r="9"/><path d="M20 22l30 26M50 22L20 48"/></g><rect x="28" y="28" width="14" height="14" rx="3" fill="#fff"/><circle cx="35" cy="35" r="3" fill="#16a596"/></svg>
    <h3>Aerial Drone Package #1</h3>
  </div>
  <div class="price"><span>Price</span><span>$175</span></div>
  <ul>
    <li>Choose up to 10 Aerial Still Images</li><li>Up to 30 seconds of Aerial Drone Video AND Up to 5 Aerial Still Images</li><li>Branded &amp; Non-Branded Property Website Links</li><li>Company Branding</li><li>Agent photo &amp; contact information</li><li>Link to agent Property Website gallery</li><li>Property description &amp; details</li><li>Weekly Seller's report</li><li>Posting to MLS</li><li>High resolution printable still photos</li><li>Unlimited text updates</li><li>Music enabled</li>
  </ul>
</div>

<div class="card" style="left:850px">
  <div class="card-head">
    <svg viewBox="0 0 70 70"><g fill="#fff"><rect x="4" y="8" width="24" height="4"/><rect x="42" y="8" width="24" height="4"/><rect x="14" y="12" width="4" height="10"/><rect x="52" y="12" width="4" height="10"/><rect x="12" y="20" width="46" height="10" rx="3"/></g><rect x="16" y="32" width="38" height="30" rx="4" fill="none" stroke="#fff" stroke-width="3"/><circle cx="35" cy="47" r="9" fill="none" stroke="#fff" stroke-width="3"/><circle cx="35" cy="47" r="4" fill="#e3202a"/></svg>
    <h3>Aerial Drone Package #2</h3>
  </div>
  <div class="price"><span>Price</span><span>$225</span></div>
  <ul>
    <li>Up to 3 minutes of Aerial Drone Video &amp; Up to 20 Aerial Still Images</li><li>Branded &amp; Non-Branded Property Website Links</li><li>Company Branding</li><li>Agent photo &amp; contact information</li><li>Link to agent Property Website gallery</li><li>Property description &amp; details</li><li>Weekly Seller's report</li><li>Posting to MLS</li><li>High resolution printable still photos</li><li>Unlimited text updates</li><li>Music enabled</li>
  </ul>
</div>

<span class="btn btn-red" style="left:491px;top:1656px;width:108px">Order Now</span>
<span class="btn btn-outline" style="left:603px;top:1656px;width:156px">Download Pricing PDF</span>

<!-- professional headshots -->
<div class="photo" style="left:122px;top:1769px;width:468px;height:404px;background:linear-gradient(180deg,#c9d0d3 0%,#8f999d 50%,#3b4450 100%)" role="img" aria-label="Businessman in a suit with arms crossed in front of an office building"></div>
<section class="headshots">
  <h2>Professional Headshots</h2>
  <p class="lead">Professional Headshots set you apart from your competition at the cost of $125</p>
  <p class="inc">All sittings will include:</p>
  <ul>
    <li>2 backdrop options</li><li>Up to 10 images to choose from</li><li>Full usage and printing rights</li><li>Digital file delivery</li>
  </ul>
</section>
<span class="btn btn-red" style="left:636px;top:2097px;width:103px">Learn More</span>
<span class="btn btn-outline" style="left:747px;top:2097px;width:121px">Find Out More</span>

<!-- why choose us -->
<h2 class="section-title" style="top:2208px">Why Choose Us?</h2>
<div class="abs why">
  <div class="why-item">
    <svg viewBox="0 0 84 84"><circle cx="42" cy="42" r="38" fill="none" stroke="#1d1d1d" stroke-width="4"/><circle cx="42" cy="42" r="32" fill="#1a6fc4"/><g stroke="#fff" stroke-width="3"><path d="M42 10l10 28M74 42l-28 10M42 74L32 46M10 42l28-10"/></g><circle cx="42" cy="42" r="9" fill="#fff"/></svg>
    <h4>WE MAKE YOU LOOK GOOD</h4>
    <p>We can help you stand out from the crowd.</p>
  </div>
  <div class="why-item">
    <svg viewBox="0 0 84 84"><path d="M6 40L36 14l30 26" stroke="#1d1d1d" stroke-width="5" fill="none"/><rect x="14" y="38" width="44" height="42" fill="#1d1d1d"/><rect x="22" y="46" width="12" height="10" fill="#fff"/><rect x="40" y="46" width="12" height="10" fill="#fff"/><rect x="30" y="62" width="12" height="18" fill="#fff"/><rect x="44" y="4" width="36" height="18" fill="#1a6fc4"/><rect x="50" y="11" width="24" height="4" fill="#fff"/></svg>
    <h4>SELL YOUR LISTINGS FASTER</h4>
    <p>Flexible availability for shoots and professional content to best represent your listings.</p>
  </div>
  <div class="why-item">
    <svg viewBox="0 0 84 84"><path d="M18 36a24 24 0 0 1 48 0" stroke="#1d1d1d" stroke-width="5" fill="none"/><rect x="12" y="32" width="10" height="18" rx="3" fill="#1d1d1d"/><rect x="62" y="32" width="10" height="18" rx="3" fill="#1d1d1d"/><rect x="16" y="56" width="52" height="24" rx="3" fill="#1d1d1d"/><circle cx="42" cy="68" r="5" fill="#1a6fc4"/></svg>
    <h4>CUSTOMER SERVICE</h4>
    <p>Reach out through our live chat, or send us a text, call, or email with any questions or concerns.</p>
  </div>
  <div class="why-item">
    <svg viewBox="0 0 84 84"><path d="M12 42a30 30 0 0 1 54-18M72 42a30 30 0 0 1-54 18" stroke="#1d1d1d" stroke-width="4" fill="none"/><path d="M66 10v14H52M18 74V60h14" stroke="#1d1d1d" stroke-width="4" fill="none"/><circle cx="42" cy="42" r="18" fill="#1a6fc4"/><circle cx="42" cy="42" r="7" fill="#fff"/></svg>
    <h4>FAST TURNAROUND TIME</h4>
    <p>We deliver all Photo and 3D Tour content before 6pm the next business day.</p>
  </div>
</div>
<span class="btn btn-red" style="left:539px;top:2494px;width:121px">Get Started</span>
<div class="abs divider"></div>

<!-- client testimonial intro -->
<section class="clients">
  <p class="label">WHAT OUR CLIENTS SAY ABOUT US</p>
  <h2>You're In Good<br>Company</h2>
  <blockquote>“Lorem ipsum dolor sit amet, consectetur adipiscing elit, sed do eiusmod tempor incididunt ut labore et dolore magna aliqua. Quis ipsum suspendisse ultrices gravida. ”</blockquote>
</section>
<span class="btn btn-red" style="left:126px;top:2843px;width:121px">Get Started</span>
<div class="photo" style="left:610px;top:2593px;width:468px;height:269px;background:linear-gradient(100deg,#cbd3d8 0%,#a8796a 45%,#3e5a7c 100%)" role="img" aria-label="Smiling homeowner holding a set of house keys"></div>
<span class="play"></span>

<!-- rotating testimonial -->
<section class="abs band" role="img" aria-label="Warm living room interior with leather sofa, dimmed"></section>
<div class="avatar" role="img" aria-label="Client portrait"></div>
<p class="band-name"><b>Owen Hale</b> | Brightmoor Group</p>
<p class="band-quote">“Lorem ipsum dolor sit amet, consectetur adipiscing elit, sed do eiusmod tempor incididunt ut labore et dolore magna aliqua. Quis ipsum suspendisse ultrices gravida. Risus commodo viverra maecenas accumsan lacus vel facilisis.”</p>
<span class="arrow" style="left:126px;transform:rotate(45deg)"></span>
<span class="arrow" style="left:1060px;transform:rotate(-135deg)"></span>
<div class="dots"><i></i><i class="on"></i><i></i></div>

<!-- partner badges -->
<div class="abs partners">
  <span class="partner"></span><span class="partner"></span><span class="partner"></span><span class="partner"></span><span class="partner"></span>
</div>

<!-- closing call to action -->
<div class="photo" style="left:0;top:3497px;width:607px;height:452px;background:linear-gradient(135deg,#c9b59b 0%,#6d6a62 40%,#b7a58c 70%,#4a4843 100%)" role="img" aria-label="Collage of interior and exterior property photographs"></div>
<section class="abs cta-dark" role="img" aria-label="Dim living room with patterned rug"></section>
<h2 class="cta-title">Ready to take the<br>next step?</h2>
<span class="btn btn-ghost" style="left:673px;top:3758px;width:124px">Pricing</span>
<span class="btn btn-red" style="left:802px;top:3758px;width:182px">Schedule Your Shoot</span>

<!-- footer -->
<footer>
  <div class="brand footer-brand"><span class="brand-mark"></span><span class="brand-name">DANA WHITFIELD<small>Real Estate Photographer</small></span></div>
  <p class="footer-about">Lorem ipsum dolor sit amet, consectetur adipiscing elit, sed do eiusmod tempor incididunt ut labore et dolore magna aliqua. Quis ipsum suspendisse ultrices gravida. Risus commodo viverra maecenas accumsan lacus vel facilisis.</p>
  <p class="fhead" style="left:427px"><u>QUICK</u> LINKS</p>
  <ul class="quick"><li>HOME</li><li>SERVICES</li><li>PROPERTY TYPE</li><li>GALLERY</li><li>PRICING</li><li>LEARN</li></ul>
  <p class="fhead" style="left:588px"><u>CONTA</u>CT US</p>
  <div class="contact">
    <div><svg width="16" height="16" viewBox="0 0 10 10"><path d="M2 0l2 2-1 2 3 3 2-1 2 2-2 2C4 10 0 6 0 2z" fill="#e3202a"/></svg>555-014-2207</div>
    <div><svg width="16" height="12" viewBox="0 0 16 12"><rect width="16" height="12" fill="#e3202a"/><path d="M0 0l8 6 8-6" stroke="#fff" stroke-width="1.5" fill="none"/></svg>hello@danawhitfield.example</div>
    <div><svg width="16" height="16" viewBox="0 0 16 16"><circle cx="8" cy="8" r="7" fill="none" stroke="#e3202a" stroke-width="1.6"/><path d="M1 8h14M8 1c-4 4-4 10 0 14M8 1c4 4 4 10 0 14" stroke="#e3202a" stroke-width="1.2" fill="none"/></svg>www.danawhitfieldproperty.example</div>
  </div>
  <p class="fhead" style="left:844px"><u>NEWSL</u>ETTER</p>
  <div class="news-input">Enter Your Email</div>
  <span class="btn btn-red news-btn">Subscribe</span>
  <p class="news-sub">Subscribe to our Newsletter</p>
  <div class="abs foot-line"></div>
  <p class="copy">Copyright © 2023 Dana Whitfield Photography . All Rights Reserved.</p>
  <div class="social"><i></i><i></i><i></i><i></i></div>
</footer>

</body>
</html>
```